Window cleaning company in need of leaflet design

Family run business requires leaflet design.
Our company uses water fed pole with pure water which is what the leaflet needs to emphasise on (include a background picture of a water fed pole cleaning a window.)

other services we offer which i would like to include are:
• facia/soffit cleaning.
• Conservatory cleans.
• Gutter clearing which is performed by a gutter vacuum pictures of gutters before and after clean are provided to every customer if they require.
• pressure washing

uploaded company logo to be included on leaflet.
number to include is 07715264389
email address is Rtglasscare@mailbay.test
would also like a facebook symbol included to show we are on social media.
Thank you

Font styles to use
Serif
Sans Serif

Colors
00a990
33a6d7
3276b5
3277b5
34a7d8
87cfc6
33b8a4
cfdfed
85acd3

Requirements
Must have
• We use traditional and water fed pole methods of cleaning. So those hard to reach or awkward to clean windows are not a problem. No need for ladders.

Our water fed pole system uses 100% pure water. This is water that has been de-ironised and de-mineralised to ensue it’s perfectly pure for a spot free finish.

• fully insured

• regular and reliable service
• one off cleans available

Call dean on 07715264389 for a free quote

```html
<!DOCTYPE html>
<html lang="en">
<head>
<meta charset="utf-8">
<title>R.T Glass Care – Window Cleaning Leaflet</title>
<link rel="stylesheet" href="https://fonts.googleapis.com/css2?family=Bebas+Neue&family=Open+Sans:wght@400;600;700&display=swap">
<style>
  :root {
    --navy: #283f96;
    --royal: #3276b5;
    --sky: #33a6d7;
    --sky-light: #85acd3;
    --mist: #cfdfed;
    --white: #ffffff;
    --ink: #3b3b3b;
    --ink-soft: #555a60;
    --logo-ink: #2a3f8f;
  }
  * { box-sizing: border-box; margin: 0; padding: 0; }
  html, body { width: 965px; height: 1200px; overflow: hidden; background: #eef0f2; }
  .leaflet {
    position: relative; width: 965px; height: 1200px; overflow: hidden;
    font-family: "Open Sans", Arial, sans-serif;
  }
  .backdrop { position: absolute; inset: 0; }
  .headline {
    position: absolute; right: 34px; top: 52px; text-align: right;
    font-family: "Bebas Neue", Impact, sans-serif; line-height: 1;
    text-shadow: 0 3px 6px rgba(0,0,0,.35);
  }
  .headline .main { display: block; color: var(--white); font-size: 66px; letter-spacing: .5px; }
  .headline .sub { display: block; color: var(--sky); font-size: 56px; margin-top: 12px; }

  .services-tab {
    position: absolute; left: 20px; top: 602px; width: 470px; height: 42px;
    background: var(--sky); border-radius: 4px;
    box-shadow: 0 4px 8px rgba(0,0,0,.3);
    font-family: "Bebas Neue", Impact, sans-serif; color: var(--white);
    font-size: 36px; line-height: 44px; text-align: center; letter-spacing: .5px;
  }
  .service-list { position: absolute; left: 60px; top: 656px; list-style: none; }
  .service-list li {
    display: flex; align-items: center; height: 64px; margin-bottom: 0;
    color: var(--white); font-weight: 700; font-size: 24px;
    text-shadow: 0 2px 3px rgba(0,0,0,.35);
  }
  .service-list li svg { width: 62px; height: 62px; margin-right: 20px; flex: none; }

  .result-labels span {
    position: absolute; font-family: "Open Sans", Arial, sans-serif; font-weight: 700;
    font-size: 11px; color: var(--white); transform: rotate(-45deg); letter-spacing: .5px;
  }

  .brand-name {
    position: absolute; left: 482px; width: 483px; top: 468px; text-align: center;
    font-family: "Open Sans", Arial, sans-serif; font-weight: 400; font-size: 40px;
    color: var(--logo-ink);
  }
  .method-heading {
    position: absolute; left: 482px; width: 483px; top: 536px; text-align: center;
    font-weight: 700; font-size: 22px; line-height: 31px; color: var(--ink);
  }
  .benefits { position: absolute; left: 512px; top: 624px; list-style: none; }
  .benefits li {
    display: flex; align-items: center; height: 32px;
    font-weight: 700; font-size: 22px; color: var(--ink-soft);
  }
  .benefits li svg { width: 18px; height: 18px; margin-right: 10px; }

  .pure-water-box {
    position: absolute; left: 511px; top: 724px; width: 418px; height: 120px;
    background: linear-gradient(180deg, #2f5fc0 0%, #243f9c 100%);
    border: 3px solid var(--mist); border-radius: 8px;
    box-shadow: 0 6px 12px rgba(0,0,0,.3);
    display: flex; align-items: center; justify-content: center; text-align: center;
    font-family: "Bebas Neue", Impact, sans-serif; color: var(--white);
    font-size: 43px; line-height: 44px;
  }
  .pure-water-note {
    position: absolute; left: 511px; top: 854px; width: 430px;
    font-weight: 600; font-size: 18.5px; line-height: 25px; color: var(--ink-soft);
  }
  .contact { position: absolute; left: 510px; top: 946px; list-style: none; }
  .contact li {
    display: flex; align-items: center; height: 34px;
    font-weight: 700; font-size: 20px; color: var(--sky);
  }
  .contact li svg { width: 24px; height: 24px; margin-right: 12px; }
  .social-square {
    position: absolute; left: 884px; top: 956px; width: 44px; height: 44px;
    border-radius: 6px; background: linear-gradient(180deg, #2a8ee0, #1c5fb8);
    box-shadow: 0 3px 6px rgba(0,0,0,.3);
  }
  .quote-line {
    position: absolute; left: 0; right: 0; top: 1140px; text-align: center;
    color: var(--white); font-size: 29px; font-weight: 400;
    display: flex; justify-content: center; align-items: center; gap: 10px;
  }
  .quote-line svg { width: 30px; height: 30px; }
</style>
</head>
<body>
<main class="leaflet">
  <svg class="backdrop" width="965" height="1200" viewBox="0 0 965 1200">
    <defs>
      <linearGradient id="navyFade" x1="0" y1="0" x2="1" y2="0">
        <stop offset="0" stop-color="#3276b5"/>
        <stop offset="1" stop-color="#283f96"/>
      </linearGradient>
      <linearGradient id="columnFade" x1="0" y1="0" x2="0" y2="1">
        <stop offset="0" stop-color="#2f58b0"/>
        <stop offset="1" stop-color="#283f96"/>
      </linearGradient>
      <linearGradient id="photoTone" x1="0" y1="0" x2="1" y2="1">
        <stop offset="0" stop-color="#dbe6f0"/>
        <stop offset=".5" stop-color="#9fb8cf"/>
        <stop offset="1" stop-color="#5a7ea6"/>
      </linearGradient>
      <linearGradient id="roofTone" x1="0" y1="0" x2="1" y2="1">
        <stop offset="0" stop-color="#6f6a5e"/>
        <stop offset="1" stop-color="#3a3d42"/>
      </linearGradient>
      <linearGradient id="cleanRoofTone" x1="0" y1="0" x2="1" y2="1">
        <stop offset="0" stop-color="#5c6168"/>
        <stop offset="1" stop-color="#2f3338"/>
      </linearGradient>
      <linearGradient id="panelFade" x1="0" y1="0" x2="0" y2="1">
        <stop offset="0" stop-color="#f4f6f9"/>
        <stop offset="1" stop-color="#ffffff"/>
      </linearGradient>
    </defs>

    <!-- base -->
    <rect width="965" height="1200" fill="url(#navyFade)"/>
    <!-- left white margin strip -->
    <rect x="0" y="540" width="36" height="620" fill="#ffffff"/>
    <!-- left services column -->
    <rect x="36" y="540" width="446" height="620" fill="url(#columnFade)"/>

    <!-- hero photograph area -->
    <path d="M0 0 H520 Q640 170 745 372 Q600 420 482 560 L0 560 Z" fill="url(#photoTone)"
          role="img" aria-label="Photo of a window cleaner in a cap using a squeegee on a large window"/>

    <!-- sky-blue swoosh and white info panel -->
    <path d="M470 610 Q660 440 965 418 V560 Q690 520 482 630 Z" fill="#33a6d7"/>
    <path d="M482 630 Q690 520 965 560 V1110 H482 Z" fill="url(#panelFade)"/>
    <path d="M482 630 Q690 520 965 560" fill="none" stroke="#cfdfed" stroke-width="4"/>

    <!-- round inset photographs -->
    <circle cx="143" cy="453" r="112" fill="#ffffff"/>
    <circle cx="143" cy="453" r="104" fill="url(#photoTone)" role="img" aria-label="Photo of a worker cleaning a fascia with a water fed pole"/>
    <circle cx="143" cy="453" r="108" fill="none" stroke="#33a6d7" stroke-width="3"/>
    <circle cx="340" cy="430" r="102" fill="#ffffff"/>
    <circle cx="340" cy="430" r="94" fill="url(#photoTone)" role="img" aria-label="Photo of a water fed pole brush cleaning a conservatory roof"/>
    <circle cx="340" cy="430" r="98" fill="none" stroke="#33a6d7" stroke-width="3"/>

    <!-- before / after gutter panel -->
    <rect x="48" y="936" width="420" height="120" rx="8" fill="#ffffff"/>
    <rect x="52" y="940" width="204" height="112" rx="6" fill="url(#roofTone)" role="img" aria-label="Photo of a gutter full of debris before clearing"/>
    <rect x="260" y="940" width="204" height="112" rx="6" fill="url(#cleanRoofTone)" role="img" aria-label="Photo of the same gutter after clearing"/>
    <path d="M52 966 L78 940 H104 L52 992 Z" fill="#33a6d7"/>
    <path d="M260 966 L286 940 H312 L260 992 Z" fill="#33a6d7"/>

    <!-- lower waves -->
    <path d="M540 1112 Q760 1030 965 1046 V1120 Q720 1094 540 1112 Z" fill="#33a6d7"/>
    <path d="M0 1200 V1138 Q460 1060 965 1112 V1200 Z" fill="url(#navyFade)"/>
    <path d="M0 1138 Q460 1060 965 1112" fill="none" stroke="#cfdfed" stroke-width="3"/>
  </svg>

  <h1 class="headline">
    <span class="main">Window Cleaning</span>
    <span class="sub">With Pure Water</span>
  </h1>

  <div class="services-tab">Other Services We Offer</div>
  <ul class="service-list">
    <li>
      <svg viewBox="0 0 62 62"><circle cx="31" cy="31" r="28" fill="#2b4aa3" stroke="#85acd3" stroke-width="2"/><path d="M16 34 L31 21 L46 34 M21 31 V42 H41 V31" fill="none" stroke="#33a6d7" stroke-width="3"/></svg>
      Facia/Soffit Cleaning
    </li>
    <li>
      <svg viewBox="0 0 62 62"><circle cx="31" cy="31" r="28" fill="#2b4aa3" stroke="#85acd3" stroke-width="2"/><path d="M17 28 Q31 14 45 28 Z M19 28 V43 H43 V28 M25 30 V43 M31 30 V43 M37 30 V43" fill="none" stroke="#ffffff" stroke-width="2.2"/></svg>
      Conservatory Cleans
    </li>
    <li>
      <svg viewBox="0 0 62 62"><circle cx="31" cy="31" r="28" fill="#2b4aa3" stroke="#85acd3" stroke-width="2"/><rect x="23" y="24" width="16" height="20" rx="3" fill="none" stroke="#ffffff" stroke-width="2.2"/><path d="M27 24 V18 H35 M31 44 V48" stroke="#ffffff" stroke-width="2.2" fill="none"/></svg>
      Pressure Washing
    </li>
    <li>
      <svg viewBox="0 0 62 62"><circle cx="31" cy="31" r="28" fill="#2b4aa3" stroke="#85acd3" stroke-width="2"/><path d="M17 22 H45 V30 H17 Z M34 30 V44" fill="none" stroke="#ffffff" stroke-width="2.4"/></svg>
      Gutter Clearing
    </li>
  </ul>
  <div class="result-labels">
    <span style="left:53px; top:954px;">BEFORE</span>
    <span style="left:265px; top:954px;">AFTER</span>
  </div>

  <div class="brand-name">R.T Glass Care</div>
  <h2 class="method-heading">WE USE TRADITIONAL AND WATER<br>FED POLE METHODS OF CLEANING</h2>
  <ul class="benefits">
    <li><svg viewBox="0 0 18 18"><circle cx="9" cy="9" r="9" fill="#283f96"/><path d="M7 5 L11 9 L7 13" fill="none" stroke="#fff" stroke-width="2"/></svg>Fully Insured</li>
    <li><svg viewBox="0 0 18 18"><circle cx="9" cy="9" r="9" fill="#283f96"/><path d="M7 5 L11 9 L7 13" fill="none" stroke="#fff" stroke-width="2"/></svg>Regular And Reliable Service</li>
    <li><svg viewBox="0 0 18 18"><circle cx="9" cy="9" r="9" fill="#283f96"/><path d="M7 5 L11 9 L7 13" fill="none" stroke="#fff" stroke-width="2"/></svg>One Off Cleans Available</li>
  </ul>

  <div class="pure-water-box">Our water fed pole system<br>uses 100% pure water!</div>
  <p class="pure-water-note">This is water that has been de-ironised and de-mineralised to ensue it’s perfectly pure for a spot free finish.</p>

  <ul class="contact">
    <li><svg viewBox="0 0 24 24"><circle cx="12" cy="12" r="12" fill="#283f96"/><path d="M8 6 L10.5 6 L11.2 9 L9.8 10 Q10.8 12.6 13.6 14 L14.6 12.7 L17.6 13.4 L17.6 16 Q11 17 7.5 8.5 Z" fill="#fff"/></svg>07715264389</li>
    <li><svg viewBox="0 0 24 24"><circle cx="12" cy="12" r="12" fill="#283f96"/><rect x="6" y="8" width="12" height="9" fill="#fff"/><path d="M6 8 L12 13 L18 8" fill="none" stroke="#283f96" stroke-width="1.4"/></svg>Rtglasscare@mailbay.test</li>
  </ul>
  <div class="social-square" aria-label="Social media"></div>

  <p class="quote-line">Call Dean on
    <svg viewBox="0 0 30 30"><circle cx="15" cy="15" r="13" fill="none" stroke="#fff" stroke-width="2"/><path d="M10 8 L13 8 L13.8 11.5 L12.2 12.7 Q13.4 15.8 16.8 17.5 L18 16 L21.6 16.8 L21.6 20 Q13.6 21.2 9.4 10.8 Z" fill="#fff"/></svg>
    07715264389 for a free quote</p>
</main>
</body>
</html>
```